Flyer-Design für Fahrschule gesucht
Zielgruppe
Wir sind eine Fahrschule/ Führerscheinausbildung/ Bildungsträger und benötigen für die verschiedenen Führerscheinklassen einen Informationsflyer.
Aufgabenstellung
Format DIN Lang zum Aufklappen
Der Flyer sollte so gestaltet sein das sich das sich die auf der Front durch Austausch eines Icon/ Logos oder Text die jeweilige Führerscheinklasse bzw Information recht einfach austauschen lässt. Rückseite auch immer gleich. Innendesign auch immer gleich bis auf die Texte die dann jeweils ausgetauscht werden müssen.
Würde ungern Fotos einsetzen da bei Fahrzeug oder personal Wechsel dieses immer wieder zu Problemen führt - ich würde lieber auf Icons setzen da diese dauerhaft bestand haben.

```html
<!DOCTYPE html>
<html lang="de">
<head>
<meta charset="utf-8">
<title>fahrzeit – Flyer DIN lang</title>
<link rel="stylesheet" href="https://fonts.googleapis.com/css2?family=Montserrat:wght@700;800&family=Raleway:wght@400;600;700&display=swap">
<style>
  :root {
    --yellow: #f6dc0a;
    --black: #111111;
    --dark: #1d1d1d;
    --grey: #2c2c2c;
    --white: #f4f4f4;
    --muted: #c9c9c9;
    --stage: #e4e4e4;
  }
  * { box-sizing: border-box; margin: 0; padding: 0; }
  html, body { width: 800px; height: 1200px; overflow: hidden; }
  body { background: var(--stage); font-family: "Raleway", sans-serif; color: var(--white); position: relative; }

  .spread { position: absolute; left: 136px; width: 528px; height: 560px; display: flex; box-shadow: 0 8px 24px rgba(0,0,0,.25); }
  .spread--outside { top: 30px; }
  .spread--inside { top: 610px; }

  .panel { position: relative; width: 264px; height: 560px; overflow: hidden;
    background: radial-gradient(ellipse at 60% 40%, #3a3a3a 0%, var(--dark) 55%, var(--black) 100%); }
  .panel + .panel { border-left: 1px solid #000; }

  .corner-ring { position: absolute; width: 90px; height: 90px; border: 10px solid var(--yellow); border-radius: 50%; }

  .brand { font-family: "Montserrat", sans-serif; font-weight: 800; color: var(--white); display: flex; align-items: center; justify-content: center; gap: 8px; }
  .brand__dot { width: 14px; height: 14px; border-radius: 50%; background: var(--yellow); }

  /* front */
  .front .brand { position: absolute; top: 150px; left: 0; right: 0; font-size: 40px; }
  .front .brand__dot { width: 22px; height: 22px; }
  .tagline { position: absolute; top: 212px; left: 0; right: 0; text-align: center; font-size: 8.5px; letter-spacing: .3px; }
  .phone-pill { display: inline-flex; align-items: center; gap: 6px; background: var(--yellow); color: var(--black);
    font-family: "Montserrat", sans-serif; font-weight: 800; font-size: 13px; padding: 3px 10px 3px 6px; }
  .phone-pill svg { width: 13px; height: 13px; }
  .front .phone-pill { position: absolute; top: 234px; left: 50%; transform: translateX(-50%); }
  .stamp { position: absolute; top: 330px; left: 50%; transform: translateX(-50%) rotate(-10deg); border: 3px solid var(--yellow);
    padding: 6px 12px; text-align: center; font-family: "Montserrat", sans-serif; font-weight: 800; line-height: 1; }
  .stamp__top { font-size: 13px; }
  .stamp__big { font-size: 26px; margin-top: 3px; }
  .web { position: absolute; bottom: 40px; left: 0; right: 0; text-align: center; font-family: "Montserrat", sans-serif; font-weight: 700; font-size: 9px; }

  /* back */
  .back .brand { position: absolute; top: 230px; left: 0; right: 0; font-size: 20px; }
  .contact { position: absolute; top: 290px; left: 0; right: 0; text-align: center; font-size: 8px; line-height: 1.45; }
  .contact__item { margin-bottom: 16px; }
  .contact__icon { display: block; width: 18px; height: 18px; margin: 0 auto 6px; background: var(--yellow); border-radius: 4px; transform: rotate(45deg); position: relative; }
  .contact__icon svg { position: absolute; inset: 3px; width: 12px; height: 12px; transform: rotate(-45deg); }
  .contact strong { font-weight: 700; }

  /* inside */
  .inside { padding: 22px 18px 0; }
  .bar { display: inline-block; background: var(--yellow); color: var(--black); font-family: "Montserrat", sans-serif; font-weight: 800;
    font-size: 14px; line-height: 1; padding: 4px 8px; text-transform: uppercase; }
  .bar-stack .bar { display: table; margin-bottom: 3px; }
  .features { position: relative; margin-top: 14px; }
  .features__line { position: absolute; left: 14px; top: 20px; bottom: 40px; border-left: 2px dotted var(--muted); }
  .feature { position: relative; display: flex; gap: 10px; margin-bottom: 12px; }
  .feature__icon { flex: none; width: 30px; height: 30px; }
  .feature h3 { font-family: "Montserrat", sans-serif; font-weight: 800; color: var(--yellow); font-size: 9px; text-transform: uppercase; margin-bottom: 3px; }
  .text { font-size: 7.2px; line-height: 1.4; color: var(--white); }
  .text--yellow { color: var(--yellow); }
  .advantages { margin-top: 6px; }
  .advantages .bar { margin-left: 20px; margin-bottom: 8px; }
  .ticks { list-style: none; margin-left: 36px; font-size: 7.4px; line-height: 1.55; }
  .ticks li { display: flex; gap: 5px; align-items: flex-start; }
  .ticks svg { flex: none; width: 8px; height: 8px; margin-top: 2px; }
  .deco-circle { position: absolute; left: -70px; bottom: 60px; width: 130px; height: 130px; border-radius: 50%; border: 22px solid #3a3a3a; }
  .bottom-band { position: absolute; left: 0; right: 0; bottom: 0; height: 10px; background: var(--yellow); }

  .inside--right .bar { margin: 0 0 8px 12px; }
  .inside--right .text { margin-bottom: 6px; }
  .inside--right section { margin-bottom: 12px; }
  .inside--right .phone-pill { margin-top: 4px; }
</style>
</head>
<body>

<!-- Outside: back panel + front panel -->
<div class="spread spread--outside">
  <div class="panel back">
    <div class="corner-ring" style="top:-55px; right:30px;"></div>
    <div class="corner-ring" style="bottom:-55px; right:-20px;"></div>
    <div class="brand"><span>fahrzeit</span><span class="brand__dot"></span></div>
    <div class="contact">
      <div class="contact__item">
        <span class="contact__icon"><svg viewBox="0 0 12 12"><path d="M6 1a3.5 3.5 0 0 0-3.5 3.5C2.5 7 6 11 6 11s3.5-4 3.5-6.5A3.5 3.5 0 0 0 6 1zm0 5a1.5 1.5 0 1 1 0-3 1.5 1.5 0 0 1 0 3z" fill="#111"/></svg></span>
        <strong>fahrzeit by Fahrschule Hollmann</strong><br>Ahornweg 12<br>48431 Rheine
      </div>
      <div class="contact__item">
        <span class="contact__icon"><svg viewBox="0 0 12 12"><path d="M3 1.5l2 2-1 1.2c.6 1.3 1.7 2.4 3 3l1.2-1 2 2-1.3 1.6C5.6 10 2 6.4 1.7 3z" fill="#111"/></svg></span>
        +49 (0) 5971 3360172
      </div>
      <div class="contact__item">
        <span class="contact__icon"><svg viewBox="0 0 12 12"><rect x="1.5" y="3" width="9" height="6" fill="#111"/><path d="M1.5 3l4.5 3.5L10.5 3" stroke="#f6dc0a" fill="none"/></svg></span>
        info@fahrzeit-schule.de
      </div>
    </div>
    <div class="web">www.fahrzeit-schule.de</div>
  </div>

  <div class="panel front">
    <div class="corner-ring" style="top:-55px; left:40px;"></div>
    <div class="corner-ring" style="bottom:-55px; right:-10px;"></div>
    <div class="brand"><span>fahrzeit</span><span class="brand__dot"></span></div>
    <div class="tagline">Führerschein • Weiterbildung • Qualifizierung</div>
    <div class="phone-pill">
      <svg viewBox="0 0 12 12"><path d="M3 1.5l2 2-1 1.2c.6 1.3 1.7 2.4 3 3l1.2-1 2 2-1.3 1.6C5.6 10 2 6.4 1.7 3z" fill="#111"/></svg>
      05971 3360172
    </div>
    <div class="stamp">
      <div class="stamp__top">FÜHRERSCHEIN IN</div>
      <div class="stamp__big">10 TAGEN</div>
    </div>
    <div class="web">www.fahrzeit-schule.de</div>
  </div>
</div>

<!-- Inside spread -->
<div class="spread spread--inside">
  <div class="panel inside">
    <div class="bar-stack">
      <span class="bar">Führerscheine in allen</span>
      <span class="bar">gängigen Klassen</span>
    </div>
    <div class="features">
      <div class="features__line"></div>
      <div class="feature">
        <svg class="feature__icon" viewBox="0 0 30 30"><polygon points="15,1 28,8 28,22 15,29 2,22 2,8" fill="#f6dc0a"/><rect x="9" y="10" width="12" height="9" rx="1" fill="none" stroke="#111" stroke-width="1.5"/><text x="15" y="17.5" font-size="6" font-family="Montserrat, sans-serif" font-weight="800" text-anchor="middle" fill="#111">B</text></svg>
        <div>
          <h3>Alle Führerscheinklassen</h3>
          <p class="text">Bei uns kannst Du alle gängigen Führerscheinklassen machen, die Du gerne machen möchtest.</p>
          <p class="text text--yellow">Auch der Führerschein ab 17 ist bei uns möglich.</p>
        </div>
      </div>
      <div class="feature">
        <svg class="feature__icon" viewBox="0 0 30 30"><polygon points="15,1 28,8 28,22 15,29 2,22 2,8" fill="#f6dc0a"/><circle cx="15" cy="16" r="6" fill="none" stroke="#111" stroke-width="1.5"/><path d="M15 16l3-3M13 9h4" stroke="#111" stroke-width="1.5"/></svg>
        <div>
          <h3>Führerschein in Rekordzeit</h3>
          <p class="text">Möchtest Du Deinen Führerschein in Rekordzeit machen? Der Intensivkurs ist genau das Richtige für alle, die ihren Führerschein in kurzer Zeit machen möchten und dafür Zeit haben. Viele unserer Schüler machen ihren Führerschein in den Ferien oder im Urlaub innerhalb von 10 Tagen.</p>
        </div>
      </div>
      <div class="feature">
        <svg class="feature__icon" viewBox="0 0 30 30"><polygon points="15,1 28,8 28,22 15,29 2,22 2,8" fill="#f6dc0a"/><path d="M8 20v-8M8 17h14v3M11 15h10v2" stroke="#111" stroke-width="1.5" fill="none"/></svg>
        <div>
          <h3>Kostengünstiges Motel</h3>
          <p class="text">Für Fahrschülerinnen und Schüler, die nicht vor Ort wohnen, bieten wir eine kostengünstige Unterkunft in unserem eigenen Fahrschul HOSTEL an.</p>
        </div>
      </div>
    </div>
    <div class="advantages">
      <span class="bar">Deine Vorteile:</span>
      <ul class="ticks">
        <li><svg viewBox="0 0 8 8"><circle cx="4" cy="4" r="4" fill="#f6dc0a"/><path d="M2 4l1.5 1.5L6 2.8" stroke="#111" fill="none"/></svg>Event-Sonderfahrten</li>
        <li><svg viewBox="0 0 8 8"><circle cx="4" cy="4" r="4" fill="#f6dc0a"/><path d="M2 4l1.5 1.5L6 2.8" stroke="#111" fill="none"/></svg><span><b>Starter-Paket</b> – All Inclusive für den Führerschein</span></li>
        <li><svg viewBox="0 0 8 8"><circle cx="4" cy="4" r="4" fill="#f6dc0a"/><path d="M2 4l1.5 1.5L6 2.8" stroke="#111" fill="none"/></svg><span><b>regelmäßiger Theorieblock</b> – nur 7 Werktage</span></li>
        <li><svg viewBox="0 0 8 8"><circle cx="4" cy="4" r="4" fill="#f6dc0a"/><path d="M2 4l1.5 1.5L6 2.8" stroke="#111" fill="none"/></svg>modernste Premium Fahrzeugflotte</li>
        <li><svg viewBox="0 0 8 8"><circle cx="4" cy="4" r="4" fill="#f6dc0a"/><path d="M2 4l1.5 1.5L6 2.8" stroke="#111" fill="none"/></svg>Jeden Woche ist Prüfung</li>
        <li><svg viewBox="0 0 8 8"><circle cx="4" cy="4" r="4" fill="#f6dc0a"/><path d="M2 4l1.5 1.5L6 2.8" stroke="#111" fill="none"/></svg><span><b>Moderner Fahr-Simulator</b> für die ersten Fahrstunden ohne Angst</span></li>
        <li><svg viewBox="0 0 8 8"><circle cx="4" cy="4" r="4" fill="#f6dc0a"/><path d="M2 4l1.5 1.5L6 2.8" stroke="#111" fill="none"/></svg>Aktuelle Lernapp für unterwegs</li>
        <li><svg viewBox="0 0 8 8"><circle cx="4" cy="4" r="4" fill="#f6dc0a"/><path d="M2 4l1.5 1.5L6 2.8" stroke="#111" fill="none"/></svg>TÜV-Begleitung</li>
        <li><svg viewBox="0 0 8 8"><circle cx="4" cy="4" r="4" fill="#f6dc0a"/><path d="M2 4l1.5 1.5L6 2.8" stroke="#111" fill="none"/></svg>Zertifiziert nach AZAV</li>
        <li><svg viewBox="0 0 8 8"><circle cx="4" cy="4" r="4" fill="#f6dc0a"/><path d="M2 4l1.5 1.5L6 2.8" stroke="#111" fill="none"/></svg>Weiterbildung nach dem Berufskraftfahrer-Qualifikationsgesetz</li>
      </ul>
    </div>
    <div class="deco-circle"></div>
    <div class="bottom-band"></div>
  </div>

  <div class="panel inside inside--right">
    <section>
      <span class="bar">Führerschein B</span>
      <p class="text"><b>Können denn Theoriestunden wirklich Spaß machen?</b> Klar – bei uns gibt's keinen trockenen Stoff, der einfach nur heruntergelesen wird. Lass Dich positiv überraschen oder sprich mal mit denen, die bei uns ihren Führerschein gemacht haben.</p>
      <p class="text">Den Stoff kann man viel besser an interessanten Beispielen lernen und sich einprägen. Willst Du wissen, was für die Prüfung wichtig ist? Bei uns gibt es viele praktische Tipps. Wir gehen mit Dir alle relevanten Themen durch und üben an echten Prüfungsfragen. Wenn es einem Schüler etwas schwerer fällt, dann geben wir gerne Nachhilfe. In unseren Filialen hast Du immer die Möglichkeit, an verschiedenen Wochentagen den Stoff zu lernen, den Du brauchst – auch wenn Du mal einen Termin verpasst hast.</p>
    </section>
    <section>
      <span class="bar">B in 10 Tagen</span>
      <p class="text">Möchtest Du Deinen Führerschein in Rekordzeit machen? Der Intensivkurs ist was für diejenigen, die ihren Führerschein in möglichst kurzer Zeit machen möchten und dafür Zeit haben.</p>
      <p class="text">Voraussetzung: Der Führerscheinantrag muss vor Beginn (ca. 6 Wochen) des Intensivkurses gestellt werden, damit der Prüfauftrag rechtzeitig erteilt wird.</p>
    </section>
    <section>
      <span class="bar">Einzel- &amp; Gruppenkurse</span>
      <p class="text">WICHTIG! Wir können die Intensivkurse nur jeweils nach unseren Kapazitäten anbieten. Daher – fragt bitte bei uns im Büro nach, ob und wann es machbar ist.</p>
      <p class="text">Bisher haben wir eine Bestehensquote von annähernd 100%. Wir bieten Gruppenkurse und Einzel-Intensivkurse an. Ganz nach persönlicher Situation können wir mit Dir Deinen Intensivkurs planen, der innerhalb unserer Kapazitäten abgestimmt wird.</p>
      <p class="text">Wir helfen Dir gerne bei der persönlichen Planung Deines Intensivkurses.</p>
      <p class="text text--yellow">Bitte mache direkt einen Termin bei uns, damit wir alles weitere besprechen können. Wir freuen uns auf deinen Anruf!</p>
      <div class="phone-pill">
        <svg viewBox="0 0 12 12"><path d="M3 1.5l2 2-1 1.2c.6 1.3 1.7 2.4 3 3l1.2-1 2 2-1.3 1.6C5.6 10 2 6.4 1.7 3z" fill="#111"/></svg>
        05971 3360172
      </div>
    </section>
    <div class="bottom-band"></div>
  </div>
</div>

</body>
</html>
```